Stationery Design Project

We are looking for a full revision of our existing stationary to include within this project:

- Letterhead
- Business card
- Compliment slip

The items should be a reflection of our new website which can be found at http://www.larkfieldchecks.co.uk/

Our logo files are included within the file brief

There are some further projects which we may approach the winning designer for as we need a revision to the front cover of our reports, a new price list and two brochures for specific target markets.

Industry/Entity Type

Business

```html
<!DOCTYPE html>
<html lang="en">
<head>
<meta charset="utf-8">
<title>Larkfield Checks – Letterhead</title>
<link rel="stylesheet" href="https://fonts.googleapis.com/css2?family=Arimo:wght@700&display=swap">
<style>
  :root {
    --paper: #ffffff;
    --navy: #000a85;
    --bright-blue: #0a35ff;
    --ink: #111111;
  }
  * { margin: 0; padding: 0; box-sizing: border-box; }
  html, body {
    width: 1200px;
    height: 1000px;
    overflow: hidden;
    background: var(--paper);
  }
  .letterhead {
    position: relative;
    width: 1200px;
    height: 1000px;
    background: var(--paper);
  }
  .brand-name {
    position: absolute;
    left: 56px;
    top: 92px;
    font-family: "Arimo", sans-serif;
    font-weight: 700;
    font-size: 56px;
    line-height: 64px;
    color: var(--navy);
    white-space: nowrap;
  }
  .contact-block {
    position: absolute;
    left: 985px;
    top: 12px;
    width: 120px;
    text-align: center;
    font-family: "Arimo", sans-serif;
    font-weight: 700;
    font-size: 17px;
    line-height: 24px;
    color: var(--ink);
    list-style: none;
  }
  .header-band {
    position: absolute;
    left: 0;
    top: 167px;
    width: 1200px;
    height: 28px;
    background: linear-gradient(to right, var(--navy) 0%, var(--navy) 46%, var(--bright-blue) 50%, var(--bright-blue) 100%);
  }
</style>
</head>
<body>
  <main class="letterhead">
    <p class="brand-name">Larkfield Checks</p>
    <ul class="contact-block">
      <li>Associate</li>
      <li>Address</li>
      <li>Address</li>
      <li>Address</li>
      <li>Phone</li>
      <li>Email</li>
    </ul>
    <div class="header-band"></div>
  </main>
</body>
</html>
```